Business Card Design For A Renovation Contractor Company

We need a business card for a new company based in Singapore, our company name is "KT Planora". We are a renovation contractor that builds designs into reality. We build more of F&B restaurants, retail stores and commercial offices. We work very closely with designers. The final design should communicate to our client that we are a company that you can trust, that will plan and complete your project without giving you a headache. I like my client to remember my company as "KT". The beauty of SIMPLE is important.

Industry/Entity Type

Contractor

Requirements
Nice to have
• Black or Red base

```html
<!DOCTYPE html>
<html lang="en">
<head>
<meta charset="utf-8">
<title>KT Planora — Business Card</title>
<link rel="stylesheet" href="https://fonts.googleapis.com/css2?family=Open+Sans:wght@300;400;600&display=swap">
<style>
  :root {
    --red: #de2a2a;
    --red-deep: #c81e22;
    --red-light: #e53a3a;
    --ink: #3a3a3a;
    --muted: #666666;
    --paper: #ffffff;
    --backdrop: #e8e8e8;
    --soft-white: rgba(255,255,255,0.85);
  }
  * { margin: 0; padding: 0; box-sizing: border-box; }
  html, body { width: 912px; height: 1200px; overflow: hidden; }
  body {
    background: var(--backdrop);
    font-family: "Open Sans", Arial, sans-serif;
    position: relative;
  }
  .card {
    position: absolute;
    left: 136px;
    width: 640px;
    height: 366px;
    box-shadow: 0 14px 28px rgba(0,0,0,0.22), 0 2px 4px rgba(0,0,0,0.12);
    overflow: hidden;
  }
  .card--front { top: 160px; background: var(--paper); }
  .card--back {
    top: 660px;
    background: linear-gradient(135deg, var(--red-light) 0%, var(--red) 45%, var(--red-deep) 100%);
  }

  /* Front: red L-shaped edge band with a thin inner rule */
  .front__band-bottom {
    position: absolute; left: 0; bottom: 0; width: 100%; height: 32px;
    background: var(--red);
  }
  .front__band-right {
    position: absolute; top: 0; right: 0; width: 34px; height: 100%;
    background: var(--red);
  }
  .front__rule-bottom {
    position: absolute; left: 0; top: 325px; width: 599px; height: 2px;
    background: var(--red);
  }
  .front__rule-right {
    position: absolute; top: 0; left: 597px; width: 2px; height: 327px;
    background: var(--red);
  }

  .brand { position: absolute; left: 58px; top: 104px; width: 270px; text-align: center; }
  .brand__dot {
    width: 62px; height: 62px; border-radius: 50%;
    background: var(--red); margin: 0 auto 16px;
  }
  .brand__name {
    font-weight: 300; font-size: 40px; line-height: 1; color: var(--ink);
    letter-spacing: 0.5px;
  }
  .brand__tagline {
    margin-top: 8px; padding-top: 4px; border-top: 1px solid var(--ink);
    font-size: 13px; color: var(--muted); font-weight: 400; display: inline-block;
  }

  .contact { position: absolute; left: 360px; top: 72px; }
  .contact__name { font-size: 22px; color: var(--red); font-weight: 400; }
  .contact__role { font-size: 16px; color: var(--ink); margin-top: 2px; }
  .contact__list { list-style: none; margin-top: 92px; }
  .contact__item {
    display: flex; align-items: center; gap: 8px;
    font-size: 17px; color: var(--ink); line-height: 24px;
  }
  .contact__icon { width: 11px; height: 11px; flex: none; }

  .back__brand {
    position: absolute; right: 44px; top: 168px; text-align: center; color: var(--paper);
  }
  .back__name { font-weight: 300; font-size: 40px; line-height: 1; }
  .back__tagline {
    display: inline-block; margin-top: 6px; padding-top: 3px;
    border-top: 1px solid var(--soft-white); font-size: 13px;
  }
  .back__web { margin-top: 20px; font-size: 16px; letter-spacing: 2px; }
</style>
</head>
<body>

<section class="card card--front" aria-label="Card front">
  <div class="front__band-bottom"></div>
  <div class="front__band-right"></div>
  <div class="front__rule-bottom"></div>
  <div class="front__rule-right"></div>

  <div class="brand">
    <div class="brand__dot"></div>
    <div class="brand__name">KT Planora</div>
    <div class="brand__tagline">planned well, built with care</div>
  </div>

  <div class="contact">
    <div class="contact__name">Daniel Tan</div>
    <div class="contact__role">Managing Director</div>
    <ul class="contact__list">
      <li class="contact__item">
        <svg class="contact__icon" viewBox="0 0 12 12"><path d="M2 1 L4.5 1 L5.5 3.5 L4 4.8 Q5.2 7 7.2 8 L8.5 6.5 L11 7.5 L11 10 Q6 11 2 6 Q1 3.5 2 1Z" fill="var(--red)"/></svg>
        6123.4567
      </li>
      <li class="contact__item">
        <svg class="contact__icon" viewBox="0 0 12 12"><rect x="1" y="4" width="10" height="6" fill="var(--red)"/><rect x="3" y="1" width="6" height="3" fill="var(--red)"/></svg>
        6123.4567
      </li>
      <li class="contact__item">
        <svg class="contact__icon" viewBox="0 0 12 12"><rect x="0.5" y="2" width="11" height="8" fill="var(--red)"/><path d="M0.5 2 L6 7 L11.5 2" stroke="#fff" fill="none"/></svg>
        info@ktplanora.com
      </li>
      <li class="contact__item">
        <svg class="contact__icon" viewBox="0 0 12 12"><circle cx="6" cy="6" r="5.5" fill="var(--red)"/><path d="M0.5 6 H11.5 M6 0.5 V11.5" stroke="#fff" stroke-width="0.8"/></svg>
        www.ktplanora.com
      </li>
    </ul>
  </div>
</section>

<section class="card card--back" aria-label="Card back">
  <div class="back__brand">
    <div class="back__name">KT Planora</div>
    <div class="back__tagline">planned well, built with care</div>
    <div class="back__web">www.ktplanora.com</div>
  </div>
</section>

</body>
</html>
```